German Webagency needs fresh modern Design

Our website is 4 years old. We need an fresh modern website. All pics we used before are from customers or handmade by us. the new website should be clear with nice handling. please dont copy something from template websites. it would be great if you can surprise us with something great. its our first project here. don´t worry if i make a mistake in responding or briefing. after 20 years you can´t see the works of your own "designer" so we hope for help :-)
our existing site: www.korvanetz.de
Target Market(s)
small and middle sized companys in germany
Number of Pages Required
4 page
Font styles to use
Colors
Designer to choose colors to be used in the design.
Requirements
Must have
- Responsive (sure we code it)
- Modern and big Font ..Headlines and Slider
- innovative..if you know something new..feel free to show
Nice to have
- the site with our works/refences should look great and later easy to handle when we code it or use wp.
- we like black and grey but if you have better ideas also feel free
Should not have
- a cup of coffe..laptop.. a pencil a handwritten font
- dont copy and modify templates from know websites..bad style

```html
<!DOCTYPE html>
<html lang="en">
<head>
<meta charset="utf-8">
<title>Korvanetz – Web Agency</title>
<link href="https://fonts.googleapis.com/css2?family=Montserrat:wght@300;400;500;600;700&family=Roboto:ital,wght@0,400;1,400&display=swap" rel="stylesheet">
<style>
:root{
  --navy:#1d3f63;
  --navy-deep:#163252;
  --sky:#2aa3dd;
  --ice:#eefafd;
  --red:#ee2a33;
  --ink:#1c3553;
  --grey-text:#8b929a;
  --band-grey:#4b4b4b;
  --band-blue:#1f6d9a;
  --band-red:#ef3340;
  --band-orange:#f6a12b;
  --btn-blue:#3a8fd3;
  --white:#ffffff;
}
*{margin:0;padding:0;box-sizing:border-box}
html,body{width:675px;height:1200px;overflow:hidden}
body{position:relative;font-family:'Montserrat',sans-serif;background:var(--white);color:var(--ink)}
.abs{position:absolute}

/* hero */
.hero-bg{left:0;top:0;width:675px;height:285px;background:linear-gradient(180deg,#28496e 0%,#1e3d61 60%,#234a73 100%)}
.hero-shape{left:0;top:240px;width:675px;height:50px}
.brand{left:56px;top:11px;color:var(--sky);font-weight:700;font-size:17px;display:flex;align-items:center;gap:6px}
.brand .dot{width:9px;height:9px;border-radius:50%;background:var(--sky)}
.nav{left:397px;top:16px;display:flex;gap:14px;font-size:7px;font-weight:600;color:var(--white)}
.nav .active{position:relative}
.nav .active::before{content:"";position:absolute;left:0;right:0;top:-16px;height:2px;background:var(--sky)}
.nav-phone{left:572px;top:16px;font-size:6px;color:#b9c6d6;display:flex;align-items:center;gap:4px}
.hero-title{left:0;width:675px;top:84px;text-align:center;color:var(--white);font-weight:600;font-size:21.5px;line-height:23px}
.hero-sub{left:0;width:675px;top:146px;text-align:center;color:var(--white);font-size:10px;line-height:15px}
.btn-red{background:var(--red);color:var(--white);font-weight:600;font-size:8px;display:flex;align-items:center;justify-content:center}
.hero-btn{left:293px;top:196px;width:81px;height:22px}
.scroll-down{left:320px;top:264px;width:28px;height:28px;border-radius:50%;background:var(--sky);border:2px solid #fff}

/* about */
.about-right{left:334px;top:285px;width:341px;height:315px;background:var(--ice)}
.about-title{left:68px;top:318px;width:210px;font-size:14.5px;font-weight:500;line-height:19px;color:var(--ink)}
.about-text{left:68px;top:387px;width:200px;font-size:6.4px;line-height:14.8px;color:var(--grey-text);font-weight:300}
.btn-outline{left:68px;top:525px;width:74px;height:20px;border:1px solid var(--ink);color:var(--ink);font-size:7.5px;display:flex;align-items:center;justify-content:center}
.about-btn{left:154px;top:525px;width:78px;height:20px}
.quote{left:402px;top:341px;width:205px;font-family:'Roboto',sans-serif;font-style:italic;font-size:10.6px;line-height:20.3px;color:var(--ink)}
.quote-author{left:403px;top:497px;font-size:9px;font-weight:600;color:var(--ink)}
.quote-author::before{content:"";display:inline-block;width:9px;height:1px;background:var(--ink);margin-right:5px;vertical-align:middle}
.quote-role{left:418px;top:510px;font-size:6.5px;color:var(--ink)}
.quote-mark{left:545px;top:460px;font-size:120px;line-height:120px;color:#dbe6ea;font-family:'Roboto',sans-serif}
.slider-dots{left:404px;top:540px;display:flex;gap:6px}
.slider-dots span{width:4px;height:4px;border-radius:50%;background:#c8dbe2}
.slider-dots .on{background:var(--ink)}

/* services band */
.services{left:0;top:590px;width:675px;height:133px}
.service-label{top:668px;width:100px;text-align:center;color:var(--white);font-size:7px;font-weight:600;line-height:9px}
.service-icon{top:630px;width:30px;height:30px}

/* partners */
.partners-title{left:0;width:675px;top:747px;text-align:center;font-size:12.5px;font-weight:500;color:var(--ink)}
.partner{top:782px;width:111px;height:48px;border:1px solid #e1e4e8;display:flex;align-items:center;justify-content:center}
.partner i{display:block;width:70px;height:16px;border-radius:3px}
.partner-dots{left:311px;top:848px;display:flex;gap:8px;align-items:center}
.partner-dots span{width:3px;height:3px;border-radius:50%;background:var(--sky)}
.partner-dots .on{width:7px;height:7px;border:1px solid var(--sky);background:radial-gradient(var(--sky) 35%,transparent 40%)}

/* contact + footer */
.contact-bg{left:0;top:885px;width:675px;height:315px;background:linear-gradient(180deg,#24476e 0%,#1d3e62 55%,#1a3858 100%)}
.contact-kicker{left:0;width:675px;top:910px;text-align:center;color:var(--white);font-size:11px}
.contact-title{left:0;width:675px;top:925px;text-align:center;color:var(--white);font-size:12px;font-weight:700}
.field{color:var(--white);font-size:5.5px;border-bottom:1px solid #6f86a1;padding-bottom:7px}
.send-btn{left:444px;top:1019px;width:75px;height:19px;background:var(--btn-blue);color:var(--white);font-size:6.5px;font-weight:600;display:flex;align-items:center;justify-content:center}
.foot-brand{left:108px;top:1073px;color:var(--sky);font-weight:700;font-size:11px;display:flex;align-items:center;gap:4px}
.foot-brand .dot{width:6px;height:6px;border-radius:50%;background:var(--sky)}
.foot-contact{left:111px;top:1100px;color:#d6deea;font-size:5.7px;line-height:12.2px}
.foot-contact div{display:flex;align-items:center;gap:5px}
.foot-col{top:1074px;color:#d6deea;font-size:5.7px;line-height:11.4px}
.foot-col h4{color:var(--white);font-size:7px;font-weight:600;margin-bottom:5px}
.foot-rule{left:111px;top:1166px;width:460px;height:1px;background:#4a6686}
.copyright{left:111px;top:1175px;color:#d6deea;font-size:5.5px}
.social{left:532px;top:1173px;display:flex;gap:4px}
.social span{width:10px;height:10px;border-radius:50%;border:1px solid #d6deea}
</style>
</head>
<body>

<!-- hero -->
<div class="abs hero-bg" role="img" aria-label="Aerial view of a city skyline at dusk in deep blue tones"></div>
<svg class="abs hero-shape" viewBox="0 0 675 50" preserveAspectRatio="none">
  <polygon points="0,12 334,36 675,12 675,50 0,50" fill="#ffffff"/>
  <polygon points="334,36 675,12 675,50 334,50" fill="#eefafd"/>
  <polyline points="0,12 334,36 675,12" fill="none" stroke="#2aa3dd" stroke-width="5"/>
</svg>
<div class="abs brand"><span class="dot"></span>korvanetz.de</div>
<nav class="abs nav"><span class="active">Home</span><span>Contact page</span><span>Random page</span></nav>
<div class="abs nav-phone">
  <svg width="7" height="7" viewBox="0 0 10 10"><path d="M2 0.5l2 2-1 1.3c.6 1.3 1.6 2.3 2.9 2.9l1.3-1 2 2-1.3 1.6C4.5 9.2.8 5.5.4 1.8z" fill="#b9c6d6"/></svg>
  +370 600 123 45
</div>
<h1 class="abs hero-title">Inspired by Outstanding Solutions for<br>Business Through Design</h1>
<p class="abs hero-sub">Our Build Websites Have Better Conversion Rates<br>Lower Bounce Rates and are Unique with Responsive Design</p>
<div class="abs btn-red hero-btn">Get Started</div>
<div class="abs scroll-down">
  <svg width="24" height="24" viewBox="0 0 24 24"><polyline points="8,10 12,14 16,10" fill="none" stroke="#fff" stroke-width="2"/></svg>
</div>

<!-- about -->
<div class="abs about-right"></div>
<h2 class="abs about-title">This is the section with few words about you and why choose you</h2>
<p class="abs about-text">Lorem ipsum dolor sit amet, consectetuer adipiscing elit. Aenean commodo ligula eget dolor. Aenean massa. Cum sociis natoque penatibus et magnis dis parturient montes, nascetur ridiculus mus. Donec quam felis, ultricies nec, pellentesque eu, pretium quis, sem. Nulla consequat massa quis enim. Donecporttitor eu, consequat vitae, eleifend ac, enim. Aliquam lorem ante, dapibus in, viverra quis, feugiat a, tellus. Phasel</p>
<div class="abs btn-outline">Read More</div>
<div class="abs btn-red about-btn">Get Started</div>

<blockquote class="abs quote">Lorem ipsum dolor sit amet, consectetuer adipiscing elit. Aenean commodo ligula eget dolor. Aenean massa. Cum sociis natoque penatibus et magnis dis parturient montes, nascetur ridiculus mus. Donec quam felis, ultricies nec, pellentesque eu, pretium quis, sem.</blockquote>
<div class="abs quote-mark">”</div>
<div class="abs quote-author">Jonas Werner</div>
<div class="abs quote-role">Company, CEO</div>
<div class="abs slider-dots"><span></span><span class="on"></span><span></span><span></span><span></span></div>

<!-- services -->
<svg class="abs services" viewBox="0 0 675 133" preserveAspectRatio="none" role="img" aria-label="Four service tiles tinted over photos of a team working at a desk">
  <polygon points="0,17 166,14 166,133 0,133" fill="#4b4b4b"/>
  <polygon points="166,14 333,9 333,133 166,133" fill="#1f6d9a"/>
  <polygon points="333,9 501,5 501,133 333,133" fill="#ef3340"/>
  <polygon points="501,5 675,0 675,133 501,133" fill="#f6a12b"/>
</svg>
<svg class="abs service-icon" style="left:66px" viewBox="0 0 30 30" fill="none" stroke="#fff" stroke-width="1.3">
  <circle cx="15" cy="13" r="8"/><circle cx="15" cy="11" r="2.5"/><path d="M10.5 17c1-2.5 8-2.5 9 0"/><line x1="9" y1="19" x2="3" y2="26"/>
</svg>
<div class="abs service-label" style="left:31px">SEO For<br>Your Business</div>
<svg class="abs service-icon" style="left:232px" viewBox="0 0 30 30" fill="none" stroke="#fff" stroke-width="1.3">
  <rect x="3" y="3" width="20" height="18"/><line x1="3" y1="7" x2="23" y2="7"/><rect x="15" y="13" width="11" height="14"/><line x1="17" y1="17" x2="24" y2="17"/><line x1="17" y1="21" x2="24" y2="21"/>
</svg>
<div class="abs service-label" style="left:196px">Responsive<br>Design</div>
<svg class="abs service-icon" style="left:402px" viewBox="0 0 30 30" fill="none" stroke="#fff" stroke-width="1.3">
  <line x1="4" y1="4" x2="26" y2="26"/><line x1="26" y1="4" x2="4" y2="26"/><rect x="2" y="2" width="5" height="5"/><path d="M23 23l4 4"/>
</svg>
<div class="abs service-label" style="left:367px">Graphic Design</div>
<svg class="abs service-icon" style="left:569px" viewBox="0 0 30 30" fill="none" stroke="#fff" stroke-width="1.3">
  <rect x="3" y="3" width="24" height="24"/><line x1="3" y1="8" x2="27" y2="8"/><circle cx="15" cy="17" r="7"/><line x1="8" y1="17" x2="22" y2="17"/><ellipse cx="15" cy="17" rx="3" ry="7"/>
</svg>
<div class="abs service-label" style="left:534px">Nice Website<br>Creation</div>

<!-- partners -->
<h2 class="abs partners-title">Our Partners</h2>
<div class="abs partner" style="left:95px"><i style="background:#f2d2d2"></i></div>
<div class="abs partner" style="left:217px"><i style="background:#cfe0f2"></i></div>
<div class="abs partner" style="left:338px"><i style="background:#d9dbe6"></i></div>
<div class="abs partner" style="left:460px"><i style="background:#d6dcf0"></i></div>
<div class="abs partner-dots"><span class="on"></span><span></span><span></span><span></span></div>

<!-- contact -->
<div class="abs contact-bg" role="img" aria-label="Aerial view of a city in muted navy tones"></div>
<div class="abs contact-kicker">Any Questions?</div>
<div class="abs contact-title">Get in Touch!</div>
<div class="abs field" style="left:170px;top:957px;width:157px">Full Name...</div>
<div class="abs field" style="left:360px;top:957px;width:159px">Email Address...</div>
<div class="abs field" style="left:170px;top:980px;width:349px;height:23px">Your Message...</div>
<div class="abs send-btn">Send Message</div>

<!-- footer -->
<div class="abs foot-brand"><span class="dot"></span>korvanetz.de</div>
<div class="abs foot-contact">
  <div><svg width="6" height="6" viewBox="0 0 10 10"><path d="M2 0.5l2 2-1 1.3c.6 1.3 1.6 2.3 2.9 2.9l1.3-1 2 2-1.3 1.6C4.5 9.2.8 5.5.4 1.8z" fill="#d6deea"/></svg>+370 600 123 45</div>
  <div><svg width="7" height="6" viewBox="0 0 10 8"><rect x="0.5" y="0.5" width="9" height="7" fill="none" stroke="#d6deea"/><polyline points="0.5,0.5 5,4.5 9.5,0.5" fill="none" stroke="#d6deea"/></svg>info@korvanetz.de</div>
  <div style="padding-left:11px">Company Name</div>
</div>
<div class="abs foot-col" style="left:250px"><h4>About Korvanetz</h4>Newsletter<br>Our Memberships<br>Events<br>Investors<br>Suppliers Response</div>
<div class="abs foot-col" style="left:378px"><h4>Account</h4>Manage Your ID<br>Korvanetz Store<br>Customer Reviews<br>Ask a Question<br>Why choose us?</div>
<div class="abs foot-col" style="left:492px"><h4>Apie Mus</h4>Inclusion and Diversity<br>Supplier Responsibility<br>Inclusion and Diversity<br>Shop for Business<br>Shop for Consumers</div>
<div class="abs foot-rule"></div>
<div class="abs copyright">Copyright 2018 Korvanetz | All rights reserved</div>
<div class="abs social"><span></span><span></span><span></span></div>

</body>
</html>
```